Business Card/Letterhead for Construction Company
Ronald Pike Construction
Professional
Ronald P. Pike
5702 Meadowlark Court, Suite #4
Germantown, TN 38138
ronald@ronaldpikeconstruction.example
www.ronaldpikeconstruction.example
Possibly add Facebook page:
www.friendpages.example/pikehouses
Navy Logo
Main Logo

```html
<!DOCTYPE html>
<html lang="en">
<head>
<meta charset="utf-8">
<title>Ronald Pike Construction – Stationery</title>
<link href="https://fonts.googleapis.com/css2?family=Lato:wght@400;700&display=swap" rel="stylesheet">
<style>
  :root {
    --navy: #1f3763;
    --navy-deep: #172a4d;
    --paper: #ffffff;
    --paper-shade: #f1f2f4;
    --flap-grey: #8d9096;
    --mark-faint: #dfe3ea;
    --ink: #3c4350;
    --label: #6d6a66;
    --stage: #e8e6e2;
  }
  * { box-sizing: border-box; margin: 0; padding: 0; }
  html, body { width: 1200px; height: 466px; overflow: hidden; }
  body {
    background: var(--stage);
    font-family: "Lato", Arial, sans-serif;
    color: var(--ink);
    position: relative;
  }
  .sheet-label {
    position: absolute;
    font-size: 6px;
    letter-spacing: 1.2px;
    text-transform: uppercase;
    color: var(--label);
    text-align: center;
  }
  .set-title { left: 20px; top: 178px; font-size: 6.5px; text-align: left; }

  .piece {
    position: absolute;
    background: var(--paper);
    overflow: hidden;
    box-shadow: 0 2px 6px rgba(0,0,0,.18);
  }
  .piece svg.band { position: absolute; left: 0; width: 100%; }

  /* name stand-in for the brand mark */
  .brand {
    position: absolute;
    display: flex;
    align-items: center;
    gap: 4px;
    font-weight: 700;
    color: var(--navy);
    text-transform: uppercase;
    white-space: nowrap;
    letter-spacing: .6px;
  }
  .brand .brand-square { background: var(--navy); flex: none; }
  .brand.faint { color: var(--mark-faint); }
  .brand.faint .brand-square { background: var(--mark-faint); }

  /* business cards */
  .card { width: 100px; height: 58px; left: 20px; }
  .card-front { top: 200px; }
  .card-back { top: 284px; }
  .card-details {
    position: absolute; left: 7px; top: 30px;
    font-size: 3.2px; line-height: 4.6px; color: var(--ink);
  }
  .card-details .person { font-weight: 700; color: var(--navy); font-size: 3.8px; }

  /* letterheads */
  .letterhead { top: 24px; width: 205px; height: 400px; }
  .letterhead-1 { left: 270px; }
  .letterhead-2 { left: 490px; }
  .letterhead .side-details {
    position: absolute; right: 14px; top: 220px;
    font-size: 3.4px; line-height: 5px; text-align: right;
  }
  .letterhead .footer-details {
    position: absolute; left: 0; right: 0; bottom: 16px;
    font-size: 3.4px; text-align: center; letter-spacing: .3px;
  }

  /* envelopes */
  .envelope-back { left: 780px; top: 24px; width: 398px; height: 240px; }
  .envelope-front { left: 780px; top: 282px; width: 398px; height: 142px; }
  .envelope-front .return-address {
    position: absolute; left: 18px; top: 52px;
    font-size: 3.6px; line-height: 5px;
  }
</style>
</head>
<body>

<div class="sheet-label set-title">Stationery Concepts</div>

<!-- Business card front -->
<section class="piece card card-front" aria-label="Business card front">
  <svg class="band" style="top:0" viewBox="0 0 100 58" width="100" height="58">
    <path d="M40 0 H100 V24 C82 10 62 4 40 0 Z" fill="var(--navy)"/>
  </svg>
  <div class="brand" style="left:7px;top:10px;font-size:5px;">
    <span class="brand-square" style="width:7px;height:7px"></span>Ronald Pike
  </div>
  <div class="card-details">
    <div class="person">Ronald P. Pike</div>
    <div>5702 Meadowlark Court, Suite #4</div>
    <div>Germantown, TN 38138</div>
    <div>ronald@ronaldpikeconstruction.example</div>
    <div>www.ronaldpikeconstruction.example</div>
  </div>
</section>
<div class="sheet-label" style="left:20px;top:262px;width:100px">Business Card Front</div>

<!-- Business card back -->
<section class="piece card card-back" aria-label="Business card back">
  <svg class="band" style="top:0" viewBox="0 0 100 58" width="100" height="58">
    <path d="M0 40 C30 48 62 50 100 42 V58 H0 Z" fill="var(--navy)"/>
  </svg>
  <div class="brand" style="left:26px;top:16px;font-size:5.5px;">
    <span class="brand-square" style="width:8px;height:8px"></span>Ronald Pike
  </div>
</section>
<div class="sheet-label" style="left:20px;top:346px;width:100px">Business Card Back</div>

<!-- Letterhead option 1 -->
<section class="piece letterhead letterhead-1" aria-label="Letterhead option 1">
  <svg class="band" style="top:0" viewBox="0 0 205 40" width="205" height="40" preserveAspectRatio="none">
    <path d="M0 0 H205 V34 C150 14 70 8 0 14 Z" fill="var(--navy)"/>
    <path d="M0 14 C70 8 150 14 205 34 V36 C150 17 70 11 0 17 Z" fill="var(--navy-deep)" opacity=".5"/>
  </svg>
  <div class="brand" style="left:66px;top:26px;font-size:6px;">
    <span class="brand-square" style="width:9px;height:9px"></span>Ronald Pike
  </div>
  <div class="side-details">
    <div>5702 Meadowlark Court, Suite #4</div>
    <div>Germantown, TN 38138</div>
    <div>ronald@ronaldpikeconstruction.example</div>
    <div>www.ronaldpikeconstruction.example</div>
    <div>www.friendpages.example/pikehouses</div>
  </div>
  <div class="brand faint" style="left:22px;top:300px;font-size:17px;">
    <span class="brand-square" style="width:22px;height:22px"></span>Ronald Pike
  </div>
</section>
<div class="sheet-label" style="left:270px;top:432px;width:205px">Letterhead Option 1</div>

<!-- Letterhead option 2 -->
<section class="piece letterhead letterhead-2" aria-label="Letterhead option 2">
  <svg class="band" style="top:0" viewBox="0 0 205 40" width="205" height="40" preserveAspectRatio="none">
    <path d="M0 0 H205 V14 C140 8 60 14 0 34 Z" fill="var(--navy)"/>
    <path d="M0 34 C60 14 140 8 205 14 V17 C140 11 60 17 0 37 Z" fill="var(--navy-deep)" opacity=".5"/>
  </svg>
  <div class="brand" style="left:66px;top:26px;font-size:6px;">
    <span class="brand-square" style="width:9px;height:9px"></span>Ronald Pike
  </div>
  <div class="brand faint" style="left:22px;top:270px;font-size:17px;">
    <span class="brand-square" style="width:22px;height:22px"></span>Ronald Pike
  </div>
  <div class="footer-details">5702 Meadowlark Court, Suite #4 · Germantown, TN 38138 · www.ronaldpikeconstruction.example</div>
</section>
<div class="sheet-label" style="left:490px;top:432px;width:205px">Letterhead Option 2</div>

<!-- Envelope back -->
<section class="piece envelope-back" aria-label="Envelope back">
  <svg class="band" style="top:0" viewBox="0 0 398 240" width="398" height="240">
    <rect width="398" height="240" fill="var(--paper-shade)"/>
    <path d="M0 0 H398 V34 C300 20 120 20 0 40 Z" fill="var(--navy)"/>
    <path d="M0 40 C120 20 300 20 398 34 V92 C300 70 110 70 0 96 Z" fill="var(--flap-grey)"/>
    <path d="M0 96 C110 70 300 70 398 92 V240 H0 Z" fill="var(--paper)"/>
    <path d="M0 180 C120 200 300 200 398 170 V240 H0 Z" fill="var(--paper-shade)"/>
  </svg>
  <div class="brand" style="left:156px;top:118px;font-size:6px;">
    <span class="brand-square" style="width:9px;height:9px"></span>Ronald Pike
  </div>
</section>

<!-- Envelope front -->
<section class="piece envelope-front" aria-label="Envelope front">
  <svg class="band" style="top:0" viewBox="0 0 398 142" width="398" height="142">
    <path d="M0 0 H260 C180 10 80 20 0 42 Z" fill="var(--navy)"/>
  </svg>
  <div class="brand" style="left:18px;top:38px;font-size:5.5px;">
    <span class="brand-square" style="width:8px;height:8px"></span>Ronald Pike
  </div>
  <div class="return-address">
    <div>5702 Meadowlark Court, Suite #4</div>
    <div>Germantown, TN 38138</div>
  </div>
  <div class="brand faint" style="left:250px;top:92px;font-size:13px;">
    <span class="brand-square" style="width:16px;height:16px"></span>Ronald Pike
  </div>
</section>
<div class="sheet-label" style="left:780px;top:432px;width:398px">Envelope Option 2</div>

</body>
</html>
```